Create a memorable Web Design for real estate branding

we are a Minnepolis brokerage and boutique housing specialist with over 27 years of experience in the Global furnished housing industry, servicing the Greater Los Angeles area. Specializing in “warm environments” we offer a customized approach to satisfying our guests and client’s needs by offering a wide array of options in highly desirable areas. Additionally, Lanterly Homes Collective offers assistance and expertise to home buyers, sellers and investors.

Industry/Entity Type

Real Estate

Number of Pages Required

1 page

Font styles to use
Serif
Sans Serif
Decorative

```html
<!DOCTYPE html>
<html lang="en">
<head>
<meta charset="utf-8">
<title>Lanterly Homes – Real Estate</title>
<link href="https://fonts.googleapis.com/css2?family=Open+Sans:wght@400;600;700&family=Raleway:wght@600;700;800&display=swap" rel="stylesheet">
<style>
:root{
  --teal:#0f9f8a;
  --teal-dark:#0a8f7d;
  --lime:#8dc63f;
  --lime-light:#9ccf3c;
  --text:#444;
  --muted:#666;
  --line:#e4e4e4;
  --white:#fff;
  --dark-band:rgba(40,40,40,.72);
}
*{box-sizing:border-box;margin:0;padding:0}
html,body{width:1200px;height:2462px;overflow:hidden}
body{position:relative;font-family:"Open Sans",Arial,sans-serif;color:var(--text);background:var(--white)}
.abs{position:absolute}
.head-font{font-family:"Raleway","Open Sans",sans-serif}

/* header */
.topline{left:0;top:0;width:1200px;height:3px;background:linear-gradient(90deg,var(--lime),var(--teal))}
.header{left:0;top:3px;width:1200px;height:89px;background:#fff;box-shadow:0 1px 3px rgba(0,0,0,.08)}
.brand{left:160px;top:24px;font-family:"Raleway",sans-serif;font-weight:800;font-size:24px;color:var(--teal);line-height:1}
.brand small{display:block;font-size:15px;margin-top:4px;letter-spacing:1px}
.nav{top:40px;font-size:11px;font-weight:600;color:#333;transform:translateX(-50%)}
.nav.active{color:var(--lime)}
.search-dot{left:1003px;top:30px;width:32px;height:32px;border-radius:50%;background:linear-gradient(135deg,var(--lime),var(--teal))}

/* hero */
.hero{left:0;top:92px;width:1200px;height:578px;background:linear-gradient(180deg,#c98a55 0%,#d9a070 30%,#8d7564 60%,#4b4a4a 100%)}
.hero-title{left:0;top:300px;width:1200px;text-align:center;color:#fff;font-family:"Raleway",sans-serif;font-weight:700;font-size:46px;line-height:50px;letter-spacing:1px}
.hero-btn{left:497px;top:418px;width:206px;height:44px;border-radius:22px;border:2px solid #fff;background:linear-gradient(90deg,var(--lime),var(--teal));color:#fff;font-weight:700;font-size:14px;line-height:40px;text-align:center}
.hero-arrow{top:335px;width:32px;height:32px;border-radius:50%;border:2px solid rgba(255,255,255,.8)}
.searchbar{left:0;top:570px;width:1200px;height:100px;background:var(--dark-band)}
.field-label{top:592px;font-size:12px;color:#fff}
.field{top:612px;height:33px;background:#fff;border:1px solid #ccc}
.field span{position:absolute;right:3px;top:9px;width:11px;height:14px;background:#e6e6e6}
.field em{position:absolute;left:10px;top:9px;font-style:normal;font-size:10px;color:#666}
.search-btn{left:950px;top:612px;width:88px;height:35px;background:linear-gradient(90deg,var(--lime),var(--teal));color:#fff;font-size:12px;font-weight:700;text-align:center;line-height:35px}

/* section titles */
.section-title{left:0;width:1200px;text-align:center;font-family:"Raleway",sans-serif;font-weight:700;font-size:22px;color:var(--teal)}
.intro{left:225px;width:750px;text-align:center;font-size:10.5px;line-height:18px;color:#555}

/* welcome cards */
.photo{position:absolute}
.card-title{font-size:13px;font-weight:700;color:var(--teal)}
.card-text{font-size:10.5px;line-height:17.5px;color:#555;width:276px}
.btn{height:27px;width:88px;background:var(--lime);color:#fff;font-size:10px;font-weight:700;text-align:center;line-height:27px}

/* services */
.services{left:0;top:1080px;width:1200px;height:498px}
.svc-title{font-size:14px;font-weight:700;color:#fff}
.svc-text{font-size:10.5px;line-height:17px;color:#eafbef;width:180px}
.svc-icon{width:80px;height:80px;border-radius:50%;border:3px solid #fff}

/* properties */
.prop{width:204px;height:325px;background:#fafafa;border:1px solid #ececec}
.tag-rent{width:42px;height:18px;background:var(--lime);color:#fff;font-size:10px;font-weight:700;line-height:18px;text-align:center}
.tag-price{width:52px;height:18px;background:var(--teal);color:#fff;font-size:10px;line-height:18px;text-align:center}
.prop-title{font-size:13.5px;font-weight:700;color:var(--teal)}
.prop-meta{font-size:9.5px;color:#555}
.round-arrow{width:32px;height:32px;border-radius:50%;border:1px solid #bbb;background:#f6f6f6}

/* footer */
.footer{left:0;top:2073px;width:1200px;height:327px;background:linear-gradient(180deg,var(--teal) 0%,var(--teal) 40%,#50b25a 75%,var(--lime-light) 100%)}
.social{top:2109px;width:27px;height:27px;border-radius:50%;border:1.5px solid #fff}
.news-title{left:380px;top:2106px;color:#fff;font-size:13px;font-weight:700;line-height:19px}
.news-input{left:604px;top:2103px;width:434px;height:42px;border:1px solid rgba(255,255,255,.8);color:#fff;font-size:11px;line-height:40px;padding-left:10px}
.news-btn{left:946px;top:2103px;width:92px;height:42px;background:var(--lime);color:#fff;font-size:11px;font-weight:700;text-align:center;line-height:42px}
.fcol h4{font-family:"Raleway",sans-serif;font-size:14px;font-weight:700;color:#fff;margin-bottom:10px}
.fcol li{list-style:none;font-size:11px;line-height:19.5px;color:#fff}
.contact li{position:relative;padding-left:16px}
.contact li i{position:absolute;left:0;top:5px;width:9px;height:9px;background:#fff;border-radius:2px}
.bottombar{left:0;top:2400px;width:1200px;height:62px;background:var(--lime-light)}
.copy{left:160px;top:2424px;font-size:10px;color:#fff}
.foot-brand{left:890px;top:2412px;font-family:"Raleway",sans-serif;font-weight:800;font-size:20px;color:#fff;line-height:1;text-align:center}
.foot-brand small{display:block;font-size:12px;margin-top:2px}
</style>
</head>
<body>

<div class="abs topline"></div>
<header class="abs header"></header>
<div class="abs brand">Lanterly Homes<small>REAL ESTATE</small></div>
<div class="abs nav active" style="left:474px">HOME</div>
<div class="abs nav" style="left:556px">SERVICE</div>
<div class="abs nav" style="left:648px">ABOUT US</div>
<div class="abs nav" style="left:750px">PROJECTS</div>
<div class="abs nav" style="left:851px">PARTNERS</div>
<div class="abs nav" style="left:948px">CONTACT</div>
<div class="abs search-dot">
  <svg width="32" height="32" viewBox="0 0 32 32"><circle cx="15" cy="15" r="4" fill="none" stroke="#fff" stroke-width="1.8"/><path d="M18 18l3 3" stroke="#fff" stroke-width="1.8"/></svg>
</div>

<!-- hero -->
<div class="abs hero" role="img" aria-label="City skyline of glass skyscrapers at golden sunset"></div>
<div class="abs hero-title">SPECIALIZING IN<br>“WARM ENVIRONMENTS”</div>
<div class="abs hero-btn">SEARCH PROPERTIES</div>
<div class="abs hero-arrow" style="left:30px"><svg width="28" height="28" viewBox="0 0 28 28"><path d="M16 9l-5 5 5 5" fill="none" stroke="#fff" stroke-width="1.8"/></svg></div>
<div class="abs hero-arrow" style="left:1140px"><svg width="28" height="28" viewBox="0 0 28 28"><path d="M12 9l5 5-5 5" fill="none" stroke="#fff" stroke-width="1.8"/></svg></div>

<div class="abs searchbar"></div>
<div class="abs field-label" style="left:163px">Property Type</div>
<div class="abs field-label" style="left:349px">Location</div>
<div class="abs field-label" style="left:480px">Select Status</div>
<div class="abs field-label" style="left:602px">Price</div>
<div class="abs field-label" style="left:722px">Sqrt</div>
<div class="abs field-label" style="left:843px">Acr</div>
<div class="abs field" style="left:163px;width:180px"><span></span></div>
<div class="abs field" style="left:347px;width:125px"><span></span></div>
<div class="abs field" style="left:478px;width:114px"><span></span></div>
<div class="abs field" style="left:600px;width:112px"><em>Min to Max</em><span></span></div>
<div class="abs field" style="left:720px;width:118px"><span></span></div>
<div class="abs field" style="left:842px;width:100px"><span></span></div>
<div class="abs search-btn">SEARCH ⊕</div>

<!-- welcome -->
<h2 class="abs section-title" style="top:702px">WELCOME TO LANTERLY HOMES</h2>
<p class="abs intro" style="top:745px">Lorem ipsum dolor sit amet, consectetur adipiscing elit, sed do eiusmod tempor incididunt ut labore et dolore magna aliqua. Ut enim ad minim veniam, quis nostrud exercitation ullamco laboris nisi ut aliquip ex ea commodo consequat. Duis aute irure dolor in reprehenderit in voluptate velit ess</p>

<div class="photo" style="left:161px;top:805px;width:276px;height:160px;background:linear-gradient(135deg,#e9e2dc,#c9b4a4)" role="img" aria-label="Hand holding house keys and a small model house"></div>
<div class="photo" style="left:462px;top:805px;width:276px;height:160px;background:linear-gradient(135deg,#cfd3d6,#8d939a)" role="img" aria-label="Agent greeting a couple at a home sale"></div>
<div class="photo" style="left:762px;top:805px;width:276px;height:160px;background:linear-gradient(135deg,#a7b8a0,#5e7f45)" role="img" aria-label="Family standing on the lawn in front of their house"></div>

<div class="abs card-title" style="left:161px;top:980px">REAL ESTATE</div>
<div class="abs card-title" style="left:462px;top:980px">BROKERAGE</div>
<div class="abs card-title" style="left:762px;top:980px">BOUTIQUE HOUSING</div>
<p class="abs card-text" style="left:161px;top:1006px">Lorem ipsum dolor sit amet, consectetur adipiscing elit, sed do eiusmod tempor incididunt ut labore et dolore magna aliqua. Ut enim ad minim veniam, quis.</p>
<p class="abs card-text" style="left:462px;top:1006px">Lorem ipsum dolor sit amet, consectetur adipiscing elit, sed do eiusmod tempor incididunt ut labore et dolore magna aliqua. Ut enim ad minim veniam, quis.</p>
<p class="abs card-text" style="left:762px;top:1006px">Lorem ipsum dolor sit amet, consectetur adipiscing elit, sed do eiusmod tempor incididunt ut labore et dolore magna aliqua. Ut enim ad minim veniam, quis.</p>

<!-- services band with curved top -->
<svg class="abs services" width="1200" height="498" viewBox="0 0 1200 498">
  <defs>
    <linearGradient id="svcGrad" x1="0" y1="0" x2="1" y2="0">
      <stop offset="0" stop-color="#8dc63f"/>
      <stop offset="1" stop-color="#0f9f8a"/>
    </linearGradient>
  </defs>
  <path d="M0 0 Q600 170 1200 0 L1200 498 L0 498 Z" fill="url(#svcGrad)"/>
</svg>
<div class="btn abs" style="left:161px;top:1075px">READ MORE</div>
<div class="btn abs" style="left:462px;top:1075px">READ MORE</div>
<div class="btn abs" style="left:762px;top:1075px">READ MORE</div>

<h2 class="abs section-title" style="top:1215px;color:#fff">REAL ESTATE &amp; BROKERAGE SERVICES</h2>

<div class="abs svc-icon" style="left:163px;top:1287px"><svg width="74" height="74" viewBox="0 0 74 74"><rect x="28" y="22" width="18" height="30" fill="#fff"/><g fill="#8dc63f"><rect x="31" y="26" width="4" height="4"/><rect x="39" y="26" width="4" height="4"/><rect x="31" y="34" width="4" height="4"/><rect x="39" y="34" width="4" height="4"/><rect x="34" y="44" width="6" height="8"/></g></svg></div>
<div class="abs svc-title" style="left:256px;top:1292px">MANAGEMENT</div>
<p class="abs svc-text" style="left:256px;top:1318px">Lorem ipsum dolor sit amet, cons tetur adipiscised do eiusmod temr incididunt ut labore et dre.</p>

<div class="abs svc-icon" style="left:471px;top:1287px"><svg width="74" height="74" viewBox="0 0 74 74"><rect x="22" y="27" width="30" height="20" rx="2" fill="none" stroke="#fff" stroke-width="2.5"/><circle cx="37" cy="37" r="5" fill="#fff"/></svg></div>
<div class="abs svc-title" style="left:564px;top:1292px">ADVISORY</div>
<p class="abs svc-text" style="left:564px;top:1318px">Lorem ipsum dolor sit amet, cons tetur adipiscised do eiusmod temr incididunt ut labore et dre.</p>

<div class="abs svc-icon" style="left:778px;top:1287px"><svg width="74" height="74" viewBox="0 0 74 74"><circle cx="37" cy="37" r="14" fill="#fff"/><path d="M30 30q5 3 3 8t4 8M42 28q-2 5 3 8" fill="none" stroke="#3db07a" stroke-width="2"/></svg></div>
<div class="abs svc-title" style="left:871px;top:1292px">MARKETING SERVICES</div>
<p class="abs svc-text" style="left:871px;top:1318px">Lorem ipsum dolor sit amet, cons tetur adipiscised do eiusmod temr incididunt ut labore et dre.</p>

<div class="abs svc-icon" style="left:163px;top:1423px"><svg width="74" height="74" viewBox="0 0 74 74"><g fill="#fff"><circle cx="37" cy="29" r="5"/><circle cx="27" cy="32" r="4"/><circle cx="47" cy="32" r="4"/><path d="M29 48q0-12 8-12t8 12z"/><path d="M20 47q0-9 7-9 3 0 4 1-3 3-3 8z"/><path d="M54 47q0-9-7-9-3 0-4 1 3 3 3 8z"/></g></svg></div>
<div class="abs svc-title" style="left:256px;top:1428px">TAX ADVISORY</div>
<p class="abs svc-text" style="left:256px;top:1454px">Lorem ipsum dolor sit amet, cons tetur adipiscised do eiusmod temr incididunt ut labore et dre.</p>

<div class="abs svc-icon" style="left:471px;top:1423px"><svg width="74" height="74" viewBox="0 0 74 74"><g fill="#fff"><ellipse cx="33" cy="33" rx="12" ry="9"/><path d="M26 40l-4 6 8-4z"/><ellipse cx="44" cy="41" rx="10" ry="7" opacity=".85"/></g></svg></div>
<div class="abs svc-title" style="left:564px;top:1428px">LEGAL ADVISORY</div>
<p class="abs svc-text" style="left:564px;top:1454px">Lorem ipsum dolor sit amet, cons tetur adipiscised do eiusmod temr incididunt ut labore et dre.</p>

<div class="abs svc-icon" style="left:778px;top:1423px"><svg width="74" height="74" viewBox="0 0 74 74"><path d="M37 22L20 37h5v13h9v-8h6v8h9V37h5z" fill="#fff"/></svg></div>
<div class="abs svc-title" style="left:871px;top:1428px">ESTATE PLANNING</div>
<p class="abs svc-text" style="left:871px;top:1454px">Lorem ipsum dolor sit amet, cons tetur adipiscised do eiusmod temr incididunt ut labore et dre.</p>

<!-- properties -->
<h2 class="abs section-title" style="top:1606px">REAL ESTATE PROPERTIES</h2>
<p class="abs intro" style="top:1650px">Lorem ipsum dolor sit amet, consectetur adipiscing elit, sed do eiusmod tempor incididunt ut labore et dolore magna aliqua. Ut enim ad minim veniam, quis nostrud exercitation ullamco laboris nisi ut aliquip ex ea commodo consequat. Duis aute irure dolor in reprehenderit in voluptate velit ess</p>

<div class="abs round-arrow" style="left:102px;top:1785px"><svg width="30" height="30" viewBox="0 0 30 30"><path d="M17 10l-5 5 5 5" fill="none" stroke="#666" stroke-width="1.5"/></svg></div>
<div class="abs round-arrow" style="left:1056px;top:1785px"><svg width="30" height="30" viewBox="0 0 30 30"><path d="M13 10l5 5-5 5" fill="none" stroke="#666" stroke-width="1.5"/></svg></div>

<div class="abs prop" style="left:161px;top:1708px"></div>
<div class="abs prop" style="left:386px;top:1708px"></div>
<div class="abs prop" style="left:610px;top:1708px"></div>
<div class="abs prop" style="left:835px;top:1708px"></div>

<div class="photo" style="left:161px;top:1708px;width:204px;height:168px;background:linear-gradient(180deg,#6fa6e0,#9aa9b0 55%,#5d8a3c)" role="img" aria-label="Two-storey family house with dormer windows"></div>
<div class="photo" style="left:386px;top:1708px;width:204px;height:168px;background:linear-gradient(180deg,#8fc0ee,#b7866d 55%,#7a8a6a)" role="img" aria-label="Row of red brick suburban houses"></div>
<div class="photo" style="left:610px;top:1708px;width:204px;height:168px;background:linear-gradient(180deg,#dfe9f2,#7f97ad 55%,#5b7b3e)" role="img" aria-label="Modern glass office building"></div>
<div class="photo" style="left:835px;top:1708px;width:204px;height:168px;background:linear-gradient(180deg,#9cc5ec,#e3e3e3 55%,#5d8b3d)" role="img" aria-label="White cottage house with front garden"></div>

<div class="abs tag-rent" style="left:164px;top:1805px">RENT</div><div class="abs tag-price" style="left:164px;top:1824px">$34,000</div>
<div class="abs tag-rent" style="left:389px;top:1805px">RENT</div><div class="abs tag-price" style="left:389px;top:1824px">$34,000</div>
<div class="abs tag-rent" style="left:613px;top:1805px">RENT</div><div class="abs tag-price" style="left:613px;top:1824px">$34,000</div>
<div class="abs tag-rent" style="left:838px;top:1805px">RENT</div><div class="abs tag-price" style="left:838px;top:1824px">$34,000</div>

<div class="abs prop-title" style="left:176px;top:1890px">BONORU MALORUM</div>
<div class="abs prop-title" style="left:400px;top:1890px">BONORU MALORUM</div>
<div class="abs prop-title" style="left:625px;top:1890px">BONORU MALORUM</div>
<div class="abs prop-title" style="left:849px;top:1890px">BONORU MALORUM</div>

<div class="abs prop-meta" style="left:176px;top:1916px">▫ 2Beds &nbsp; ▫ 2Baths &nbsp; ▫ 1418FT2</div>
<div class="abs prop-meta" style="left:400px;top:1916px">▫ 2Beds &nbsp; ▫ 2Baths &nbsp; ▫ 1418FT2</div>
<div class="abs prop-meta" style="left:625px;top:1916px">▫ 2Beds &nbsp; ▫ 2Baths &nbsp; ▫ 1418FT2</div>
<div class="abs prop-meta" style="left:849px;top:1916px">▫ 2Beds &nbsp; ▫ 2Baths &nbsp; ▫ 1418FT2</div>

<p class="abs card-text" style="left:176px;top:1940px;width:180px">Lorem ipsum dolor sit amet, cons ectetur adipiscing elitsed do.</p>
<p class="abs card-text" style="left:400px;top:1940px;width:180px">Lorem ipsum dolor sit amet, cons ectetur adipiscing elitsed do.</p>
<p class="abs card-text" style="left:625px;top:1940px;width:180px">Lorem ipsum dolor sit amet, cons ectetur adipiscing elitsed do.</p>
<p class="abs card-text" style="left:849px;top:1940px;width:180px">Lorem ipsum dolor sit amet, cons ectetur adipiscing elitsed do.</p>

<div class="abs btn" style="left:176px;top:1990px">READ MORE</div>
<div class="abs btn" style="left:400px;top:1990px">READ MORE</div>
<div class="abs btn" style="left:625px;top:1990px">READ MORE</div>
<div class="abs btn" style="left:849px;top:1990px">READ MORE</div>

<!-- footer -->
<footer class="abs footer"></footer>
<div class="abs social" style="left:163px"></div>
<div class="abs social" style="left:197px"></div>
<div class="abs social" style="left:231px"></div>
<div class="abs social" style="left:265px"></div>
<div class="abs" style="left:334px;top:2095px;width:1px;height:62px;background:rgba(255,255,255,.4)"></div>
<div class="abs news-title">LANTERLY HOMES SIGN UP<br>FOR OUR NEWSLETTER</div>
<div class="abs news-input">Email address</div>
<div class="abs news-btn">SUBSCRIBE</div>

<div class="abs fcol" style="left:160px;top:2218px"><h4>LINKS</h4><ul><li>Home</li><li>About us</li><li>Real Estate</li><li>Brokerage</li><li>Properties</li><li>Contact Us</li></ul></div>
<div class="abs fcol" style="left:318px;top:2218px"><h4>MY PROPERTY</h4><ul><li>Saved properties</li><li>Saved Searches and Alerts</li><li>Open Home Planner</li><li>My Account</li><li>My Agent Profile</li></ul></div>
<div class="abs fcol" style="left:530px;top:2218px"><h4>SERVICES</h4><ul><li>Sed ut perspiciatis unde</li><li>Dis iste natus error sit vo</li><li>Lptatem accusantiumd</li><li>Roremque laudantium</li><li>Totam rem aperiam</li><li>Dipsa quae ab illo</li></ul></div>
<div class="abs fcol" style="left:733px;top:2218px"><h4>RESOURCES</h4><ul><li>Home</li><li>User Agreement</li><li>Resources</li><li>Home Loan</li><li>NRI Services</li><li>How To Buy</li></ul></div>
<div class="abs fcol contact" style="left:871px;top:2218px;width:175px"><h4>CONTACT</h4><ul><li><i></i>48 Alder Grove Ave, Suite 210, Fairview, MN 55401</li><li><i></i>Phone: (555) 210-0147</li><li><i></i>Fax: (555) 210-0146</li><li><i></i>hello@lanterlyhomes.example</li></ul></div>

<div class="abs bottombar"></div>
<div class="abs copy">© 2016 Lanterly Homes. All rights are reserved.</div>
<div class="abs foot-brand">Lanterly Homes<small>REAL ESTATE</small></div>

</body>
</html>
```